Glimmer Synchronized Swim Team's Clubhouse (web page)

Fun, Super Easy to read and navigate. Please error on the side of too large font sizes rather than too small font sizes.

We are a New Orleans (USA) based club for adults and youth of all genders.

We have youth and adult performance and competition teams. We teach synchronized swimming. We perform at special events.

Webpage should allow for

1. Sign up for classes, camps and teams (pay fees, sign waivers, reserve a spot and link to national Corvane Aquaform club membership website in order to buy required national membership).Make our multi step registration process easy, quick, pleasant.

2. Provide an area to upload practice schedules.
and performance calendar.

3. Easily
Hire one of our synchro squad to perform at special events.

4. Embedded Google Calndar

5 Members only site
( one away for youth and one area for adults. )

6 Show off our new logo, photos and videos. Be able to change these images often.

Our team colors are red, aqua and pink.

7. Buy logo gear

Click to team shop at
Drevik gear.com and other future team shops.

8. One click to become a sponsor of the team.

An area to show off sponsor logos. We will have several levels of sponsorships. It is important to have small medium and large logo spots. WE also will have a wall of names of folks who donate 10 - 100 dollars to sponsor the team.

We want the experience to be fun . We do not want headache producing events.

Our team colors are red, pink and aqua. WE have not settled on a specific red or pink yet. You are free to play around with different tones and hues. I tend toward a sholcking pink and cherry red. But really do want to see what your thoughts are for our reds and pinks. Also feel free to vary aqua from a light to dark. But we do want to stay away from navy.
Thanks for your hard work and creativity.

Target Market(s)

All ages, genders and ethnicity. Swimmers, dancers and event planners.

Coding

Coded - Design and coding required

Number of Pages Required

4 page

Font styles to use
Sans Serif

Colors
ec1f27
0293ce
f59195

Requirements
Must have
• See p descriptions +
• Fine #20 is our logo and
• Playful, bold, elegant, Colorful (red, aqua and pink are our team colors).
• I want to be able to plug in / update photos , schedules, release forms, almost everything as our seasons change. I do not know ( Newbury) do I want coded or incised site. All advice welcome.
Nice to have
• Your flare as a designer. Thank you for making us better through your creativity, ability to edit, clarify and advice. :-)
Should not have
• Confusion.

```html
<!DOCTYPE html>
<html lang="en">
<head>
<meta charset="utf-8">
<title>Glimmer Synchronized Swim Team – Clubhouse</title>
<link href="https://fonts.googleapis.com/css2?family=Open+Sans:wght@400;600;700&family=Raleway:wght@500;600;700&display=swap" rel="stylesheet">
<style>
:root{
  --aqua:#0293ce;
  --aqua-light:#29b6e8;
  --aqua-dark:#0a6fb0;
  --red:#ec1f27;
  --pink:#f59195;
  --pink-soft:#f2757b;
  --ink:#3a3a3a;
  --muted:#8a8a8a;
  --grey-bg:#efefef;
  --line:#d8d8d8;
  --white:#ffffff;
}
*{margin:0;padding:0;box-sizing:border-box}
html,body{width:1200px;height:3429px;overflow:hidden}
body{position:relative;background:var(--white);font-family:"Open Sans",Arial,sans-serif;color:var(--ink)}
.abs{position:absolute}
.heading{font-family:"Raleway","Open Sans",sans-serif;font-weight:600;letter-spacing:1px;text-transform:uppercase}

/* sky header */
.sky{left:0;top:0;width:1200px;height:600px;background:linear-gradient(180deg,#bfe3f1 0%,#dff1f8 45%,#ffffff 100%)}
.account-tab{left:900px;top:0;width:140px;height:52px;background:rgba(255,255,255,.55);border-radius:0 0 6px 6px;font-size:14px;color:var(--aqua);text-align:center;line-height:56px;letter-spacing:.5px}
.nav{left:149px;top:69px;width:902px;height:57px;background:linear-gradient(180deg,#1aa9e4,var(--aqua-dark));display:flex;align-items:center;font-size:16px;font-weight:600;color:var(--white)}
.nav a{color:var(--white);text-decoration:none;padding:0 13px;line-height:57px}
.nav a.active{background:rgba(0,0,0,.18)}
.nav .spacer{flex:1}
.logo-badge{left:515px;top:14px;width:170px;height:150px;background:var(--white);border-radius:50%;border:4px solid #e8f4fa;display:flex;flex-direction:column;align-items:center;justify-content:center}
.logo-badge .dot{width:34px;height:34px;border-radius:50%;background:var(--aqua-light);margin-bottom:8px}
.logo-badge .name{font-family:"Raleway",sans-serif;font-weight:700;font-size:20px;color:var(--aqua-dark);letter-spacing:1px}

.hero{left:149px;top:126px;width:902px;height:445px}
.hero-text{left:149px;top:270px;width:902px;text-align:center;color:var(--white);font-family:"Raleway",sans-serif;font-weight:600;text-transform:uppercase;text-shadow:0 2px 6px rgba(0,0,0,.35)}
.hero-text .l1{font-size:31px;letter-spacing:1px}
.hero-text .l2{font-size:34px;margin-top:6px;letter-spacing:1px}
.hero-dots{left:0;top:516px;width:1200px;display:flex;justify-content:center;gap:8px}
.hero-dots span{width:13px;height:13px;border-radius:50%;background:var(--white);opacity:.85}
.hero-dots span:first-child{background:transparent;border:2px solid var(--white)}

/* steps */
.section-title{left:0;width:1200px;text-align:center;font-size:22px;color:#444}
.steps-line{left:258px;top:708px;width:680px;height:2px;background:#b9dcef}
.step{width:220px;text-align:center}
.step-ring{width:132px;height:132px;margin:0 auto;border-radius:50%;border:3px solid #cfe9f6;display:flex;align-items:center;justify-content:center;background:var(--white)}
.step-ring .inner{width:104px;height:104px;border-radius:50%;border:3px solid var(--aqua);display:flex;align-items:center;justify-content:center}
.step-node{width:16px;height:16px;border-radius:50%;border:2px solid var(--aqua);background:var(--white);top:701px}
.step h3{margin-top:20px;font-size:18px;font-weight:600;color:var(--aqua-dark)}
.step h3 b{color:var(--red);font-weight:700}
.step p{margin-top:6px;font-size:12px;line-height:18px;color:var(--muted)}
.divider{left:149px;top:914px;width:902px;height:1px;background:var(--line)}

/* about */
.about-title{left:152px;top:944px;font-family:"Raleway",sans-serif;font-weight:700;font-size:28px;color:var(--red)}
.about-photo{left:149px;top:990px;width:224px;height:267px;border-radius:18px;background:linear-gradient(160deg,#8fa3b3,#c6b7ae 55%,#5e6f86)}
.about-copy{left:400px;top:995px;width:370px;font-size:13.5px;line-height:22px;color:var(--muted)}
.about-copy p+p{margin-top:12px}
.btn-pink{background:var(--pink-soft);color:var(--white);font-weight:600;border-radius:3px;text-align:center;font-size:15px}
.upload-btn{left:393px;top:1214px;width:245px;height:43px;line-height:43px}

.cal-title{left:789px;top:953px;font-family:"Raleway",sans-serif;font-weight:700;font-size:23px;color:var(--aqua-dark);letter-spacing:.5px}
.calendar{left:789px;top:1001px;width:262px;border-collapse:collapse;font-size:14px;text-align:center}
.calendar .month{background:var(--aqua);color:var(--white);height:32px;font-weight:600;font-size:14px}
.calendar .month span{display:flex;justify-content:space-between;padding:0 10px}
.calendar .days th{background:var(--red);color:var(--white);font-weight:600;height:26px;font-size:13px}
.calendar td{border:1px solid #cfcfcf;height:29px;width:37px;color:var(--ink)}
.calendar td.off{color:#aaa}
.calendar td.today{background:#222;color:var(--white)}

/* hire */
.hire-band{left:0;top:1300px;width:1200px;height:312px}
.hire-text{left:0;top:1392px;width:1200px;text-align:center;color:var(--white);font-family:"Raleway",sans-serif;text-transform:uppercase}
.hire-text .l1{font-size:27px;font-weight:600;letter-spacing:1px}
.hire-text .l2{font-size:22px;font-weight:600;margin-top:6px;letter-spacing:1px}
.btn-outline{border:2px solid var(--white);color:var(--white);font-weight:600;text-align:center;font-size:15px;letter-spacing:1px}
.hire-btn{left:533px;top:1477px;width:144px;height:41px;line-height:37px}

/* members */
.members{left:0;top:1612px;width:1200px;height:347px;background:var(--grey-bg)}
.members-photo{left:178px;top:1662px;width:238px;height:238px;border-radius:50%;border:6px solid var(--white);box-shadow:0 2px 8px rgba(0,0,0,.2);background:radial-gradient(circle at 50% 45%,#e2a3a3,#b96b73 45%,#7d9aa8 80%)}
.members-title{left:437px;top:1690px;font-family:"Raleway",sans-serif;font-weight:700;font-size:24px;color:#444}
.members-copy{left:437px;top:1736px;width:580px;font-size:13.5px;line-height:24px;color:var(--muted)}
.pill{height:44px;border-radius:22px;border:2px solid;display:flex;align-items:center;justify-content:center;gap:10px;font-weight:700;font-size:16px;background:var(--white)}
.pill .ico{width:30px;height:30px;border-radius:50%;display:flex;align-items:center;justify-content:center}
.pill-youth{left:439px;top:1822px;width:149px;border-color:var(--red);color:var(--red)}
.pill-youth .ico{background:var(--red)}
.pill-adults{left:594px;top:1822px;width:149px;border-color:var(--aqua);color:var(--aqua)}
.pill-adults .ico{background:var(--aqua)}

/* videos */
.videos-title{top:2005px;color:var(--pink-soft);font-size:27px;font-weight:700}
.video{overflow:hidden}
.video .frame{width:100%;height:100%}
.video-side-left{left:226px;top:2094px;width:172px;height:185px}
.video-side-right{left:805px;top:2094px;width:167px;height:185px}
.video-main{left:398px;top:2060px;width:407px;height:253px;box-shadow:0 4px 16px rgba(0,0,0,.35);z-index:2}
.play{position:absolute;border-radius:50%;background:var(--white);display:flex;align-items:center;justify-content:center}
.controls{position:absolute;left:0;bottom:0;width:100%;height:22px;background:#f4f4f4;display:flex;align-items:center;padding:0 8px;gap:8px}
.controls .bar{flex:1;height:4px;background:#333;border-radius:2px}
.controls .tri{width:0;height:0;border-left:8px solid #333;border-top:5px solid transparent;border-bottom:5px solid transparent}
.controls .vol{width:10px;height:8px;background:#333}
.shop-btn{left:523px;top:2352px;width:151px;height:44px;line-height:44px}

/* gallery */
.gallery-band{left:0;top:2420px;width:1200px;height:403px}
.gallery-title{top:2476px;color:var(--white);font-size:27px;font-weight:700}
.gallery{left:149px;top:2533px;width:902px;height:180px;display:flex}
.gallery div{flex:1;height:180px}
.donors-btn{left:471px;top:2741px;width:128px;height:39px;line-height:35px;font-size:13px}
.donate-btn{left:603px;top:2741px;width:128px;height:39px;line-height:35px;font-size:13px}

/* sponsors */
.sponsors{left:0;top:2823px;width:1200px;height:252px;background:var(--grey-bg)}
.sponsor-title{top:2884px;color:#9a9a9a;font-size:27px;font-weight:600}
.sponsor-row{left:149px;top:2945px;width:902px;height:56px;display:flex;justify-content:space-between;align-items:center;color:#a9a9a9}
.sponsor-row span{font-family:"Raleway",sans-serif;font-weight:700;font-size:26px}
.sponsor-row span.sm{font-size:17px;letter-spacing:.5px}

/* footer */
.footer-col{top:3140px;font-size:14px;line-height:26px;color:#555}
.footer-col h4{font-family:"Raleway",sans-serif;font-weight:600;font-size:20px;color:var(--aqua);margin-bottom:12px}
.social{display:flex;gap:8px;margin-top:10px}
.social span{width:30px;height:30px;border-radius:50%}
.footer-logo{left:823px;top:3132px;width:171px;height:141px;display:flex;flex-direction:column;align-items:center;justify-content:center}
.footer-logo .dot{width:56px;height:56px;border-radius:50%;background:var(--aqua-light);margin-bottom:12px}
.footer-logo .name{font-family:"Raleway",sans-serif;font-weight:700;font-size:24px;color:var(--aqua-dark);letter-spacing:1px}
.bottom-bar{left:0;top:3360px;width:1200px;height:69px;background:#e9e9e9;text-align:center;line-height:69px;font-size:12px;color:#777}
</style>
</head>
<body>

<header>
  <div class="abs sky" role="img" aria-label="Soft sky with clouds behind the header"></div>
  <div class="abs account-tab">SIGN UP &nbsp;|&nbsp; LOGIN</div>
  <nav class="abs nav">
    <a class="active">Home</a><a>About Us</a><a>Services</a><a>Blogs</a>
    <span class="spacer"></span>
    <a>Video</a><a>Photos</a><a>Shop</a><a>Resources</a>
  </nav>
  <div class="abs logo-badge"><span class="dot"></span><span class="name">GLIMMER</span></div>
</header>

<section>
  <svg class="abs hero" viewBox="0 0 902 445" role="img" aria-label="Hero photo of a plush toy fish and a red toy on a woven mat">
    <defs>
      <linearGradient id="heroFill" x1="0" y1="0" x2="1" y2="1">
        <stop offset="0" stop-color="#b67a54"/>
        <stop offset=".5" stop-color="#d9a14e"/>
        <stop offset="1" stop-color="#7d5a4a"/>
      </linearGradient>
    </defs>
    <path d="M0 0H902V420Q451 470 0 420Z" fill="url(#heroFill)"/>
  </svg>
  <div class="abs hero-text"><div class="l1">Pellentesque faucibus ut accumsan</div><div class="l2">Ultricies elit maecenas</div></div>
  <div class="abs hero-dots"><span></span><span></span><span></span><span></span></div>
</section>

<section>
  <h2 class="abs section-title heading" style="top:592px">Sign up for classes</h2>
  <div class="abs steps-line"></div>
  <span class="abs step-node" style="left:363px"></span>
  <span class="abs step-node" style="left:590px"></span>
  <span class="abs step-node" style="left:816px"></span>

  <div class="abs step" style="left:148px;top:642px">
    <div class="step-ring"><div class="inner">
      <svg width="52" height="52" viewBox="0 0 52 52" fill="none" stroke="var(--aqua-dark)" stroke-width="3"><rect x="10" y="6" width="32" height="40" rx="3"/><path d="M26 14v24M31 19q-5-4-9 0t4 7q9 3 4 7t-9 0" stroke="var(--red)"/></svg>
    </div></div>
    <h3><b>1.</b> Pay Fees</h3>
    <p>Mauris vel lacus vitae felis vesti<br>bulum volutpat Etiam</p>
  </div>
  <div class="abs step" style="left:375px;top:642px">
    <div class="step-ring"><div class="inner">
      <svg width="52" height="52" viewBox="0 0 52 52" fill="none" stroke="var(--red)" stroke-width="3"><circle cx="18" cy="18" r="9"/><path d="M24 24l18 18M34 34l5-5M39 39l4-4"/></svg>
    </div></div>
    <h3><b>2.</b> Sign Waivers</h3>
    <p>Mauris vel lacus vitae felis vesti<br>bulum volutpat Etiam</p>
  </div>
  <div class="abs step" style="left:601px;top:642px">
    <div class="step-ring"><div class="inner">
      <svg width="52" height="52" viewBox="0 0 52 52" fill="none" stroke="var(--red)" stroke-width="3"><path d="M18 8v26M34 8v26M18 16h16M18 24h16"/><path d="M6 36q5-4 10 0t10 0 10 0 10 0M6 44q5-4 10 0t10 0 10 0 10 0" stroke="var(--aqua-dark)"/></svg>
    </div></div>
    <h3><b>3.</b> Reserve a Spot</h3>
    <p>Mauris vel lacus vitae felis vesti<br>bulum volutpat Etiam</p>
  </div>
  <div class="abs step" style="left:827px;top:642px">
    <div class="step-ring"><div class="inner">
      <svg width="52" height="52" viewBox="0 0 52 52" fill="none" stroke="var(--aqua-dark)" stroke-width="3"><rect x="6" y="8" width="34" height="24" rx="3"/><path d="M24 20l16 20 3-8 8-2z" fill="var(--red)" stroke="var(--red)"/></svg>
    </div></div>
    <h3><b>4.</b> National Club</h3>
    <p>link to national Corvane Aquaform club<br>membership website</p>
  </div>
  <div class="abs divider"></div>
</section>

<section>
  <h2 class="abs about-title">ABOUT GLIMMER</h2>
  <div class="abs about-photo" role="img" aria-label="Two young swimmers in sparkly team suits"></div>
  <div class="abs about-copy">
    <p>Curabitur iaculis tempus eros Curabitur vel mi sit amet magna malesuada ultrices Ut nisi erat.</p>
    <p>scelerisque mi tortor at ipsum cligula augue bibendum accumsan vestibulum ut commodo a mi Morbi ornare gravida elit Integer congue augue et malesuada iaculis ipsum dui aliquet felis at cursus magna nisl nec elit Praesent elementum elit at tellus nec ultricies sit amet porttitor mattis enim In massa libero interdum nec interdum ve</p>
  </div>
  <div class="abs btn-pink upload-btn">Upload Practice Schedule</div>

  <h2 class="abs cal-title">ORBLY CALENDAR</h2>
  <table class="abs calendar">
    <tr class="month"><th colspan="7"><span><b>&#9664;</b>DECEMBER 2016<b>&#9654;</b></span></th></tr>
    <tr class="days"><th>Su</th><th>Mo</th><th>Tu</th><th>We</th><th>Th</th><th>Fr</th><th>Sa</th></tr>
    <tr><td class="off">28</td><td class="off">29</td><td class="off">30</td><td class="off">31</td><td>1</td><td>2</td><td>3</td></tr>
    <tr><td>4</td><td>5</td><td>6</td><td>7</td><td>8</td><td>9</td><td>10</td></tr>
    <tr><td>11</td><td>12</td><td>13</td><td>14</td><td>15</td><td>16</td><td>17</td></tr>
    <tr><td>18</td><td>19</td><td class="today">20</td><td>21</td><td>22</td><td>23</td><td>24</td></tr>
    <tr><td>25</td><td>26</td><td>27</td><td>28</td><td>29</td><td>30</td><td class="off">1</td></tr>
    <tr><td class="off">2</td><td class="off">3</td><td class="off">4</td><td class="off">5</td><td class="off">6</td><td class="off">7</td><td class="off">8</td></tr>
  </table>
</section>

<section>
  <svg class="abs hire-band" viewBox="0 0 1200 312" preserveAspectRatio="none" role="img" aria-label="Bright pool water surface">
    <defs>
      <linearGradient id="water" x1="0" y1="0" x2="0" y2="1">
        <stop offset="0" stop-color="#1aa3dd"/>
        <stop offset=".5" stop-color="#3cc3ec"/>
        <stop offset="1" stop-color="#0e8fc9"/>
      </linearGradient>
    </defs>
    <path d="M0 28Q150 0 300 22T600 20T900 18T1200 26V312H0Z" fill="url(#water)"/>
  </svg>
  <div class="abs hire-text"><div class="l1">Hire one of our synchro squad to</div><div class="l2">perform at special events</div></div>
  <div class="abs btn-outline hire-btn">HIRE</div>
</section>

<section>
  <div class="abs members"></div>
  <div class="abs members-photo" role="img" aria-label="Team swimmers in red caps posing in a circle formation"></div>
  <h2 class="abs members-title">MEMBERS ONLY SITE</h2>
  <p class="abs members-copy">Curabitur iaculis tempus eros Curabitur vel mi sit amet magna malesuada ultrices Ut nisi erat fermentum vel congue id euismod in elit Fusce ultricies orci ac feugiat suscipit leo massa sodales velit et scelerisque mi tortor at ipsum cligula augue</p>
  <div class="abs pill pill-youth"><span class="ico"><svg width="16" height="16" viewBox="0 0 16 16" fill="#fff"><circle cx="8" cy="5" r="3.5"/><path d="M2 15q6-9 12 0z"/></svg></span>YOUTH</div>
  <div class="abs pill pill-adults"><span class="ico"><svg width="16" height="16" viewBox="0 0 16 16" fill="#fff"><circle cx="8" cy="5" r="3.5"/><path d="M2 15q6-9 12 0z"/></svg></span>ADULTS</div>
</section>

<section>
  <h2 class="abs section-title heading videos-title">Latest videos</h2>
  <div class="abs video video-side-left">
    <div class="frame" role="img" aria-label="Video still of swimmers at the pool edge" style="background:linear-gradient(180deg,#6a7c8a 0%,#49b3da 55%,#2a9ccc 100%)"></div>
    <div class="play" style="left:112px;top:70px;width:36px;height:36px"><svg width="14" height="14" viewBox="0 0 14 14"><path d="M3 1l10 6-10 6z" fill="#222"/></svg></div>
    <div class="controls"><span class="tri"></span><span class="bar"></span></div>
  </div>
  <div class="abs video video-side-right">
    <div class="frame" role="img" aria-label="Video still of a swimmer gliding through the water" style="background:linear-gradient(180deg,#57c2e8,#1f93c9)"></div>
    <div class="play" style="left:10px;top:70px;width:36px;height:36px"><svg width="14" height="14" viewBox="0 0 14 14"><path d="M3 1l10 6-10 6z" fill="#222"/></svg></div>
    <div class="controls"><span class="tri"></span><span class="bar"></span><span class="vol"></span></div>
  </div>
  <div class="abs video video-main">
    <div class="frame" role="img" aria-label="Video still of young swimmers in caps in the pool" style="background:linear-gradient(160deg,#2a9fb8,#49b6c9 50%,#1b7f9c)"></div>
    <div class="play" style="left:176px;top:88px;width:56px;height:56px"><svg width="22" height="22" viewBox="0 0 14 14"><path d="M3 1l10 6-10 6z" fill="#222"/></svg></div>
    <div class="controls"><span class="tri"></span><span class="bar"></span><span class="vol"></span></div>
  </div>
  <div class="abs btn-pink shop-btn">TEAM SHOP</div>
</section>

<section>
  <svg class="abs gallery-band" viewBox="0 0 1200 403" preserveAspectRatio="none" aria-hidden="true">
    <defs>
      <linearGradient id="galleryFill" x1="0" y1="0" x2="1" y2="0">
        <stop offset="0" stop-color="#1491cf"/>
        <stop offset=".55" stop-color="#6b8fc0"/>
        <stop offset="1" stop-color="#f39296"/>
      </linearGradient>
    </defs>
    <path d="M0 30Q150 0 300 22T600 18T900 20T1200 16V403H0Z" fill="url(#galleryFill)"/>
  </svg>
  <h2 class="abs section-title heading gallery-title">Photo gallery</h2>
  <div class="abs gallery">
    <div role="img" aria-label="Swimmers racing in pool lanes" style="background:linear-gradient(180deg,#7fa0b4,#3eb6e0)"></div>
    <div role="img" aria-label="Close view of a swimmer's arm in the water" style="background:linear-gradient(160deg,#3f8a7e,#b79c86)"></div>
    <div role="img" aria-label="Swimmers' legs raised above the water" style="background:linear-gradient(160deg,#4c7f8a,#cfa58f)"></div>
    <div role="img" aria-label="Swimmer floating on the pool surface" style="background:linear-gradient(180deg,#36b4d9,#1f8fc4)"></div>
  </div>
  <div class="abs btn-outline donors-btn">DONORS</div>
  <div class="abs btn-outline donate-btn">DONATE</div>
</section>

<section>
  <div class="abs sponsors"></div>
  <h2 class="abs section-title heading sponsor-title">Sponsor</h2>
  <div class="abs sponsor-row">
    <span>Vantor</span>
    <span class="sm">The Kessly Post</span>
    <span>Moro News</span>
    <span>Roam + Rest</span>
    <span>Qel.</span>
    <span class="sm">The Harbor Ledger</span>
  </div>
</section>

<footer>
  <div class="abs footer-col" style="left:160px">
    <h4>Quick Links</h4>
    <div>About Us</div><div>How to Sign In</div><div>Photos</div><div>Videos</div><div>Calendar</div>
  </div>
  <div class="abs footer-col" style="left:370px">
    <h4>Resources</h4>
    <div>Our Blogs</div><div>Sponsors</div><div>Team</div><div>Buy Now</div>
  </div>
  <div class="abs footer-col" style="left:576px">
    <h4>Follow Us</h4>
    <div>Please connect with us on these</div>
    <div class="social"><span style="background:var(--aqua-light)"></span><span style="background:var(--aqua)"></span><span style="background:var(--aqua-dark)"></span><span style="background:var(--red)"></span></div>
  </div>
  <div class="abs footer-logo"><span class="dot"></span><span class="name">GLIMMER</span></div>
  <div class="abs bottom-bar">© 2016 Company Name. All right reserved. Term of Use.</div>
</footer>

</body>
</html>
```